Tobias Webpage Design

I would like to start an business and management consultancy business. I am thinking to called it "Krelto Consultancy". Besides the consultancy services, I would also like to provide training on finance, forensic accounting, fraud prevention and internal control.
Professional management consultants are contracted by organizations to provide advisory services in an objective and independent manner.

Services include, but are not limited to, strategic planning, facilitation, quality assurance, education and training, investment counsel, identification and analysis of management problems, developing solutions, and the implementation of proposed solutions.

Professional management consultants are hired when an organization lacks sufficient resources, requires external objective advice, or because they have expertise not available within the client organization.

I would like to see the webpage design that use colors apple green with some other contrast color. The design have to be professional look but with a new age touch.

Reason: Unable to find a suitable web pages design

Dear all

Since last week I post a request, but till to date, I has yet to received a new sparkling creative and "wow" web page design. Please help me here!

Regards

Reason: Yet to found a suitable web designer for my web design. Help! I just need a fresh and professional look design. You may ignore the color code I prefer. Send me your sparkling creative work. Thank you so much!

Some examples

```html
<!DOCTYPE html>
<html lang="en">
<head>
<meta charset="utf-8">
<title>Krelto Consultancy</title>
<link rel="stylesheet" href="https://fonts.googleapis.com/css2?family=Arimo:wght@400;700&family=Cabin:wght@400&display=swap">
<style>
  :root {
    --apple-green: #4cc82a;
    --apple-green-light: #8fe07a;
    --apple-green-dark: #1f9a12;
    --tab-active: #5fe32a;
    --ink: #111111;
    --white: #ffffff;
    --card-top: #d9dadc;
    --card-bottom: #f7f7f8;
    --footer-bg: #000000;
    --hero-blue: #2f5fc4;
    --hero-light: #eef1f6;
  }
  * { box-sizing: border-box; margin: 0; padding: 0; }
  html, body { width: 1188px; height: 1200px; overflow: hidden; background: var(--white); }
  .page { position: relative; width: 1188px; height: 1200px; font-family: "Cabin", sans-serif; color: var(--ink); }

  .site-header {
    position: absolute; left: 0; top: 0; width: 1188px; height: 224px;
    background: linear-gradient(180deg, var(--apple-green-light) 0%, var(--apple-green) 70%, #3bbd1c 100%);
  }
  .brand {
    position: absolute; left: 28px; top: 80px;
    font-family: "Arimo", sans-serif; font-weight: 700; font-size: 40px;
    color: var(--white); letter-spacing: 0.5px;
  }

  .main-nav { position: absolute; left: 0; top: 182px; width: 1188px; height: 72px; }
  .nav-tab {
    position: absolute; top: 0; width: 176px; height: 70px;
    border-radius: 8px;
    background: linear-gradient(180deg, #3fd21c 0%, var(--apple-green-dark) 100%);
    display: flex; align-items: center; gap: 6px; padding-left: 6px;
    font-family: "Arimo", sans-serif; font-size: 25px; color: var(--white);
  }
  .nav-tab.is-active { background: linear-gradient(180deg, #6ff03a 0%, var(--tab-active) 100%); }
  .nav-tab svg { flex: none; }

  .welcome {
    position: absolute; left: 0; top: 278px; width: 1143px; text-align: center;
    font-size: 37px; letter-spacing: -0.5px;
  }

  .hero {
    position: absolute; left: 6px; top: 340px; width: 1182px; height: 492px;
    background: linear-gradient(90deg, #3866c9 0%, #6d8fd6 35%, var(--hero-light) 60%, #f4f4f4 80%, #c98a86 92%, var(--hero-light) 100%);
  }

  .feature-card {
    position: absolute; top: 847px; width: 315px; height: 305px;
    border-radius: 22px;
    background: linear-gradient(180deg, var(--card-top) 0%, var(--card-bottom) 55%, #f2f2f3 100%);
  }
  .feature-card svg { position: absolute; left: 50%; transform: translateX(-50%); }
  .feature-label {
    position: absolute; left: 0; width: 100%; top: 210px; text-align: center;
    font-size: 38px; color: var(--ink);
  }

  .site-footer {
    position: absolute; left: 0; top: 1164px; width: 1188px; height: 36px;
    background: var(--footer-bg); color: var(--white);
    text-align: center; font-size: 25px; line-height: 36px;
  }
</style>
</head>
<body>
<div class="page">
  <header class="site-header">
    <div class="brand">KRELTO CONSULTANCY</div>
  </header>

  <nav class="main-nav">
    <div class="nav-tab is-active" style="left:39px">
      <svg width="58" height="52" viewBox="0 0 58 52"><path d="M4 26 L29 4 L54 26 L47 26 L47 50 L35 50 L35 34 L23 34 L23 50 L11 50 L11 26 Z" fill="#14300a"/></svg>
      <span>Home</span>
    </div>
    <div class="nav-tab" style="left:232px">
      <svg width="54" height="54" viewBox="0 0 54 54"><circle cx="27" cy="27" r="24" fill="#2a6b1c" stroke="#9ee28a" stroke-width="2"/><circle cx="27" cy="15" r="4" fill="#fff"/><rect x="23" y="22" width="8" height="20" rx="2" fill="#fff"/></svg>
      <span>About</span>
    </div>
    <div class="nav-tab" style="left:423px">
      <svg width="54" height="54" viewBox="0 0 54 54"><circle cx="27" cy="27" r="24" fill="#a8ec7a"/></svg>
      <span>Traning</span>
    </div>
    <div class="nav-tab" style="left:615px">
      <svg width="56" height="56" viewBox="0 0 56 56"><g fill="#2c7a1a"><circle cx="28" cy="28" r="20"/><rect x="24" y="2" width="8" height="52"/><rect x="2" y="24" width="52" height="8"/><rect x="24" y="2" width="8" height="52" transform="rotate(45 28 28)"/><rect x="24" y="2" width="8" height="52" transform="rotate(-45 28 28)"/></g><circle cx="28" cy="28" r="13" fill="#e8f5e0"/><circle cx="28" cy="28" r="8" fill="#2c7a1a"/><circle cx="28" cy="28" r="4" fill="#e8f5e0"/></svg>
      <span>Services</span>
    </div>
    <div class="nav-tab" style="left:806px">
      <svg width="54" height="48" viewBox="0 0 54 48"><path d="M2 18 L27 6 L52 18 L27 30 Z" fill="#0f4a0a"/><path d="M12 23 L12 36 Q27 44 42 36 L42 23 L27 30 Z" fill="#0f4a0a"/></svg>
      <span>Education</span>
    </div>
    <div class="nav-tab" style="left:996px">
      <svg width="46" height="46" viewBox="0 0 46 46"><circle cx="23" cy="23" r="20" fill="#2f6f22" stroke="#b7e6a6" stroke-width="2"/></svg>
      <span>Facilitation</span>
    </div>
  </nav>

  <h1 class="welcome" style="font-weight:400">WELCOME TO WEBSITE</h1>

  <div class="hero" role="img" aria-label="Illustration of a presenter at a whiteboard teaching a seated classroom audience"></div>

  <section class="feature-card" style="left:26px">
    <svg width="180" height="136" viewBox="0 0 180 136" style="top:28px">
      <rect x="2" y="2" width="176" height="128" rx="6" fill="#fbfbfb" stroke="#d0d0d0" stroke-width="2"/>
      <path d="M4 6 L90 76 L176 6" fill="none" stroke="#cfcfcf" stroke-width="2"/>
      <path d="M4 128 L70 60 M176 128 L110 60" fill="none" stroke="#e0e0e0" stroke-width="2"/>
    </svg>
    <div class="feature-label">CONTACT US</div>
  </section>

  <section class="feature-card" style="left:432px">
    <svg width="190" height="180" viewBox="0 0 190 180" style="top:6px">
      <g fill="#8a8d92">
        <circle cx="95" cy="90" r="68"/>
        <rect x="80" y="4" width="30" height="172" rx="4"/>
        <rect x="9" y="75" width="172" height="30" rx="4"/>
        <rect x="80" y="4" width="30" height="172" rx="4" transform="rotate(45 95 90)"/>
        <rect x="80" y="4" width="30" height="172" rx="4" transform="rotate(-45 95 90)"/>
      </g>
      <circle cx="95" cy="90" r="58" fill="#b9bcc0"/>
      <circle cx="95" cy="90" r="46" fill="#1e6fd8"/>
      <circle cx="95" cy="90" r="34" fill="#dfe3e8"/>
      <circle cx="95" cy="90" r="16" fill="#b3b8bf"/>
      <circle cx="95" cy="90" r="9" fill="#e9ecef"/>
    </svg>
    <div class="feature-label">SERVICES</div>
  </section>

  <section class="feature-card" style="left:842px">
    <svg width="260" height="160" viewBox="0 0 260 160" style="top:8px">
      <path d="M8 66 L140 10 L252 60 L120 120 Z" fill="#2a2a2c"/>
      <path d="M60 88 L60 124 Q130 156 200 118 L200 82 L120 120 Z" fill="#151516"/>
      <circle cx="128" cy="62" r="8" fill="#3a3a3c"/>
      <path d="M128 62 L64 92 L60 136" fill="none" stroke="#e0a21a" stroke-width="5"/>
      <path d="M53 136 L67 136 L70 160 L50 160 Z" fill="#e0a21a"/>
    </svg>
    <div class="feature-label">EDUCATION</div>
  </section>

  <footer class="site-footer">All Right Reserved Copyright 2013</footer>
</div>
</body>
</html>
```